依頼詳細
5月の2日間開催する駅前イベントのフライヤーです。当イベントは年間来場者150万円を誇るすずらんボタニカルの隣り駅で行います。特にゴールデンウィーク期間は大藤の見頃で、多くの方が来場します。イベントは、パークへ来場した観光客へ中心市街地(観光地)回遊して貰うことを目的とします。

・フライヤーを見た方が「おいしそう」「おもしろそう」「隣駅だし、ちょっと寄ってみるか」と思って貰えるようなデザインをお願いします

・裏面の飲食店紹介は、Adobe Fontsを使ってください(差し替える可能性があるため)
・写真が用意できてないため、それっぽい写真をダミーで挿入してください(こちらで差し替えます)
・フライヤーのオモテ面隅に割引券が入ります
・マップはおよそこのくらいの範囲というものをスクリーンショットしました。マップに必ず入れたい情報は、(1)会場(2)KT柚ノ原駅(3)観光駐車場(4)東隣の駅が「すずらんボタニカル駅、であることです
・イベントロゴはワイヤーフレームaiファイルに入っています
・ロゴが青ですが、飲食イベントと考えると暖色系もありなのかとは思います。その場合でもロゴの色は変えないでください。もしくはあえて寒色系でまとめておしゃれ感を出すのもありです
・印刷は上質紙で行う予定です
記載項目
添付のPDFにおよその情報配置、入れて欲しい言葉を掲載しました。
サイズ
A4
ページ数
両面
希望イメージ
• +5 0 +5
• シンプル
複雑
• 単色
カラフル
• 暗い
明るい
• 日常
高級
• 遊び心
厳粛
• 未来的
伝統的
• 女性的
男性的
希望する色
赤系、緑系、黄・オレンジ系
納品ファイル
• 高解像度JPG (.jpg)
• イラストレーター形式 (.ai)
補足説明
依頼公開後の追記内容
■ 選んだ理由

発注者の弊社が今まで手がけたデザインなど、提案ページの情報だけではなく調べて提案して頂けたのだなと思えるこちらが希望する方向性だったため。

■ 提案者全員のお礼・コメント

たくさんの提案ありがとうございました。そろそろ、すずらんボタニカルの大藤(日本最大面積)の見頃を迎えますので、お近くの方はぜひ足利市へいらしてください。

```html
<!DOCTYPE html>
<html lang="ja">
<head>
<meta charset="utf-8">
<title>クラフトビール＆ゆのはらグルメ｜柚ノ原駅前マーケット</title>
<link href="https://fonts.googleapis.com/css2?family=Yusei+Magic&family=M+PLUS+Rounded+1c:wght@500;800&display=swap" rel="stylesheet">
<style>
:root{
  --navy:#3b5f8a;
  --sky:#dcecf2;
  --cream:#fbfaf3;
  --yellow:#fbec7a;
  --yellow-deep:#f4d23c;
  --white:#ffffff;
}
*{margin:0;padding:0;box-sizing:border-box}
html,body{width:846px;height:1200px;overflow:hidden}
body{background:var(--cream);font-family:"M PLUS Rounded 1c",sans-serif;color:var(--navy)}
.flyer{position:relative;width:846px;height:1200px;overflow:hidden;background:linear-gradient(180deg,var(--sky) 0%,var(--cream) 55%)}
.photo{position:absolute}
.photo--beer{left:480px;top:180px;width:366px;height:560px;background:radial-gradient(circle at 55% 50%,#f2c45a 0%,#c98a2c 35%,#6f7c74 70%,#9fb3a8 100%)}
.photo--guitar{left:0;top:420px;width:260px;height:430px;background:radial-gradient(circle at 45% 55%,#d9a66c 0%,#a46a3d 45%,#d8cbb6 85%)}
.photo--food{left:0;top:846px;width:846px;height:282px;background:linear-gradient(100deg,#e6d6a8 0%,#c98a3f 28%,#a35a2a 50%,#7d8f3a 72%,#c2452f 88%,#6a3a22 100%)}
.garland{position:absolute;left:170px;top:112px;width:480px;height:58px;background:linear-gradient(180deg,#cfe6ee 0%,#f2ecbf 100%);border-radius:0 0 50% 50%/0 0 100% 100%}
.blob{position:absolute;left:90px;top:140px}
.logo{position:absolute;top:36px;left:0;width:100%;display:flex;justify-content:center;align-items:center;gap:8px;font-weight:800;font-size:24px;letter-spacing:2px}
.logo .mark{width:12px;height:12px;background:var(--navy)}
.headline{font-family:"Yusei Magic",sans-serif;font-weight:400}
.headline span{position:absolute;line-height:1;white-space:nowrap}
.headline .l1{left:196px;top:228px;font-size:58px}
.headline .l2{left:196px;top:292px;font-size:95px}
.headline .l3{left:440px;top:402px;font-size:86px}
.headline .amp{left:630px;top:246px;font-size:90px;color:var(--yellow-deep);font-family:"M PLUS Rounded 1c",sans-serif;font-weight:800;-webkit-text-stroke:3px var(--navy)}
.access{position:absolute;left:690px;top:432px;width:110px;text-align:center;font-weight:800;font-size:16px;line-height:1.25}
.access b{display:block;font-size:58px;line-height:1}
.venue{position:absolute;left:0;width:846px;top:574px;text-align:center;font-weight:800;font-size:26px}
.dates{position:absolute;left:210px;top:622px;display:flex;align-items:flex-end;gap:16px;font-weight:800}
.date small{display:block;font-size:13px}
.date .d{font-size:50px;line-height:1}
.date .wd{font-size:14px;vertical-align:top;margin-left:2px}
.dates .sep{font-size:34px;line-height:1.3}
.times{position:absolute;left:258px;top:720px;display:flex;gap:30px;align-items:center;font-weight:800;font-size:40px;line-height:1}
.times small{font-size:11px;margin-right:6px}
.info{position:absolute;left:0;width:846px;top:778px;text-align:center;font-size:13px;line-height:1.5}
.bubble{position:absolute;background:var(--white);font-weight:800;border-radius:50%;display:flex;align-items:center;justify-content:center;text-align:center;line-height:1.2;font-size:18px}
.bubble--beer{left:592px;top:128px;width:138px;height:82px}
.bubble--music{left:112px;top:452px;width:112px;height:64px}
.bubble--gourmet{left:624px;top:978px;width:134px;height:74px}
.coupon{position:absolute;right:0;top:0;width:128px;height:114px;background:var(--white);border-left:2px dashed var(--navy);border-bottom:2px dashed var(--navy);text-align:center;padding-top:8px;font-weight:800}
.coupon .t{font-size:11px}
.coupon .p{font-size:32px;line-height:1.1}
.coupon .p span{font-size:14px}
.coupon .n{font-size:9px;font-weight:500;margin-top:3px}
.footer{position:absolute;left:0;top:1128px;width:846px;height:72px;background:var(--white);display:flex;align-items:center;justify-content:center}
.search{display:flex;border:2px solid var(--navy);height:34px}
.search .q{padding:0 18px;font-size:15px;font-weight:800;display:flex;align-items:center;width:240px}
.search .btn{background:var(--navy);color:var(--white);font-size:13px;padding:0 14px;display:flex;align-items:center}
</style>
</head>
<body>
<main class="flyer">
  <div class="photo photo--beer" role="img" aria-label="クラフトビールのグラスを掲げる写真"></div>
  <div class="photo photo--guitar" role="img" aria-label="ギターを演奏する手元の写真"></div>
  <div class="photo photo--food" role="img" aria-label="麺料理や焼き野菜、揚げ物などの地元グルメの写真"></div>

  <svg class="blob" width="720" height="710" viewBox="0 0 720 710" aria-hidden="true">
    <path d="M90 60 C240 0 500 10 640 90 C730 170 725 400 680 540 C620 680 400 720 230 690 C70 660 0 540 10 360 C18 220 25 110 90 60Z" fill="var(--yellow)"/>
  </svg>

  <header class="logo"><span class="mark"></span>柚ノ原駅前マーケット</header>

  <div class="garland" role="img" aria-label="三角の旗が連なるガーランドの飾り"></div>

  <div class="coupon">
    <div class="t">当日限定 クラフトビール</div>
    <div class="p">200<span>円</span></div>
    <div class="t">割引券</div>
    <div class="n">本券ご提示で一杯割引</div>
  </div>

  <div class="bubble bubble--beer">クラフト<br>ビールも!</div>
  <div class="bubble bubble--music">音楽も!</div>
  <div class="bubble bubble--gourmet">グルメも!</div>

  <h1 class="headline">
    <span class="l1">クラフトビール</span>
    <span class="l2">ゆのはら</span>
    <span class="l3">グルメ</span>
    <span class="amp">&amp;</span>
  </h1>

  <p class="access">KT柚ノ原駅<br>徒歩<b>3</b>分</p>

  <p class="venue">@柚ノ原駅前マーケット</p>

  <div class="dates">
    <div class="date"><small>2019</small><span class="d">5月4日</span><span class="wd">SAT</span></div>
    <span class="sep">▶</span>
    <div class="date"><small>2019</small><span class="d">5月5日</span><span class="wd">SUN</span></div>
  </div>

  <div class="times">
    <span><small>OPEN</small>11:00</span>
    <span><small>CLOSE</small>16:00</span>
  </div>

  <p class="info">詳しい出店情報は<br>各SNS、又はホームページをご覧ください<br>https://ekimae-yunohara.example/</p>

  <footer class="footer">
    <div class="search"><span class="q">柚ノ原駅前マーケット</span><span class="btn">検索</span></div>
  </footer>
</main>
</body>
</html>
```